Personal Trainer and Corporate Health Business

I need a business card for a new company I'm starting in Australia called "Brisk Vitality Partners" I will be providing a Personal training service as well as corporate health in companies.
The service provided is to help promote an active and healthy lifstyle.
The design should communicate a healthy lifestyle and also the benefits that this can have on a personal level and in the corporate environment and the benefits that flow from that.

Target Market(s)

Members of the public and Corporate

Industry/Entity Type

Environment

Requirements
Must have
• Company logo attached
Look and feel fresh and modern

Tag line: "Energising people for a brighter routine"

Lewis Norgate
Managing Director

m: 0417 596 304
e: lewis@briskvitalitypartners.com.au

www.briskvitalitypartners.com.au
Nice to have
• Can be 1 or 2 sided

```html
<!DOCTYPE html>
<html lang="en">
<head>
<meta charset="utf-8">
<title>Brisk Vitality Partners – Business Card</title>
<link rel="stylesheet" href="https://fonts.googleapis.com/css2?family=Open+Sans:ital,wght@0,400;0,600;0,700;1,600&display=swap">
<style>
  :root {
    --backdrop: #2a2a2a;
    --card-white: #ffffff;
    --brand-green: #a6ce39;
    --brand-blue: #1b5aa8;
    --text-grey: #6d6e71;
    --faint-grey: #ededed;
    --card-shadow: 0 14px 30px rgba(0, 0, 0, 0.55);
  }

  * { box-sizing: border-box; margin: 0; padding: 0; }

  html, body {
    width: 1200px;
    height: 900px;
    overflow: hidden;
    background: var(--backdrop);
    font-family: "Open Sans", Arial, sans-serif;
  }

  .canvas {
    position: relative;
    width: 1200px;
    height: 900px;
  }

  .card {
    position: absolute;
    width: 620px;
    height: 354px;
    box-shadow: var(--card-shadow);
    overflow: hidden;
  }

  /* Front side */
  .card--front {
    left: 60px;
    top: 70px;
    background: var(--card-white);
  }

  .brand-mark {
    position: absolute;
    left: 44px;
    top: 84px;
    display: flex;
    align-items: center;
    gap: 10px;
  }

  .brand-mark__dot {
    flex: none;
    width: 20px;
    height: 20px;
    border-radius: 50%;
    background: var(--brand-green);
  }

  .brand-mark__name {
    font-weight: 700;
    font-size: 24px;
    line-height: 1.1;
    letter-spacing: 0.5px;
    text-transform: uppercase;
    color: var(--brand-blue);
  }

  .faint-name {
    position: absolute;
    right: 34px;
    top: 24px;
    font-weight: 700;
    font-size: 42px;
    line-height: 1.05;
    text-align: right;
    text-transform: uppercase;
    color: var(--faint-grey);
  }

  .contact {
    position: absolute;
    left: 44px;
    top: 196px;
  }

  .contact__name {
    font-weight: 700;
    font-size: 19px;
    letter-spacing: 0.5px;
    text-transform: uppercase;
    color: var(--brand-green);
    line-height: 1.1;
  }

  .contact__role {
    font-weight: 600;
    font-size: 11px;
    letter-spacing: 0.4px;
    text-transform: uppercase;
    color: var(--text-grey);
    margin-bottom: 14px;
  }

  .contact__list {
    list-style: none;
    font-size: 11.5px;
    line-height: 1.45;
    text-transform: uppercase;
  }

  .contact__label {
    display: inline-block;
    width: 62px;
    font-weight: 600;
    color: var(--brand-green);
  }

  .contact__value {
    color: var(--text-grey);
    font-weight: 600;
  }

  .front-band {
    position: absolute;
    left: 0;
    right: 0;
    bottom: 0;
    height: 30px;
    background: var(--brand-green);
  }

  /* Back side */
  .card--back {
    left: 520px;
    top: 476px;
    background: var(--brand-green);
  }

  .back-brand {
    position: absolute;
    left: 0;
    right: 0;
    top: 104px;
    display: flex;
    justify-content: center;
    align-items: center;
    gap: 14px;
  }

  .back-brand__dot {
    flex: none;
    width: 24px;
    height: 24px;
    border-radius: 50%;
    background: var(--brand-blue);
  }

  .back-brand__name {
    font-weight: 700;
    font-size: 34px;
    line-height: 1.1;
    letter-spacing: 0.5px;
    text-transform: uppercase;
    color: var(--card-white);
  }

  .tagline {
    position: absolute;
    left: 0;
    right: 0;
    bottom: 58px;
    text-align: center;
    font-style: italic;
    font-weight: 600;
    font-size: 14px;
    color: var(--brand-blue);
  }
</style>
</head>
<body>
<main class="canvas">

  <section class="card card--front" aria-label="Business card front">
    <div class="faint-name" aria-hidden="true">Brisk<br>Vitality</div>

    <div class="brand-mark">
      <span class="brand-mark__dot"></span>
      <span class="brand-mark__name">Brisk Vitality<br>Partners</span>
    </div>

    <div class="contact">
      <p class="contact__name">Lewis Norgate</p>
      <p class="contact__role">Managing Director</p>
      <ul class="contact__list">
        <li><span class="contact__label">Mobile :</span><span class="contact__value">0417 596 304</span></li>
        <li><span class="contact__label">Email :</span><span class="contact__value">lewis@briskvitalitypartners.com.au</span></li>
        <li><span class="contact__label">Website :</span><span class="contact__value">www.briskvitalitypartners.com.au</span></li>
      </ul>
    </div>

    <div class="front-band"></div>
  </section>

  <section class="card card--back" aria-label="Business card back">
    <div class="back-brand">
      <span class="back-brand__dot"></span>
      <span class="back-brand__name">Brisk Vitality<br>Partners</span>
    </div>
    <p class="tagline">“Energising people for a brighter routine”</p>
  </section>

</main>
</body>
</html>
```